Unique Realtor Website for real state Broker

All Real Estate websites look the same with the same boring layout and info that no one cares about. What I am looking for is a Realtor/Broker site but more focused on me and my services along with client reviews and testimonials. I am primarily a buyers Broker and a Military Specialist (VA) and that's what I want to focus on. I need a tab where I can put my listings, but I don't want listings to be the focus like most sites are. I also run a nonprofit dog rescue and I want a tab to talk about that as well. I am also looking to have a more mid-century feel to my site as mid-century architecture is my passion. I sell in both San Diego and Palm Springs. There's an artist based out of Palm Springs whom I love and I would like the feel of my site to have a similar vibe (attached are some of Bluvens pieces to give you a better idea). I'm also having a cartoon drawing done of myself that I would like on the site as well (should be ready in a couple days). Want to make sure that the site is SEO focused as well. my current site is: www.tovarelhomes.com for reference.

Target Market(s)

Buyers

Industry/Entity Type

Real Estate Agent

Coding

Coded - Design and coding required

Number of Pages Required

5+ page

Font styles to use
Sans Serif

Colors
fece3e
fee18a
ffffff
000000
959595

Requirements
Must have
• Must be unique, fun, buyer focused with SEO capability and strong social media base
• web site need to be designed for Word Press

```html
<!DOCTYPE html>
<html lang="en">
<head>
<meta charset="utf-8">
<title>Halvor Real Estate</title>
<link rel="stylesheet" href="https://fonts.googleapis.com/css2?family=Montserrat:wght@400;500;600;700&family=Great+Vibes&display=swap">
<style>
:root{
  --gold:#e8b931;
  --gold-soft:#fee18a;
  --ink:#1e1c1b;
  --ink-2:#2a2725;
  --grey:#959595;
  --grey-light:#ebebeb;
  --white:#ffffff;
  --text:#5a5a5a;
}
*{box-sizing:border-box;margin:0;padding:0}
html,body{width:1200px;height:4024px;overflow:hidden;background:var(--white)}
body{font-family:"Montserrat",sans-serif;color:var(--text);position:relative}
section{position:absolute;left:0;width:1200px;overflow:hidden}
.photo{position:absolute}
.script{font-family:"Great Vibes",cursive;font-weight:400;font-size:72px;line-height:1;color:var(--ink)}
.kicker{font-size:17px;font-weight:700;letter-spacing:5px;text-transform:uppercase;color:var(--ink)}
.body-copy{font-size:15px;line-height:26px;color:var(--text)}
.btn{display:inline-block;background:var(--gold);color:var(--ink);font-size:12px;font-weight:700;letter-spacing:2px;text-transform:uppercase;padding:14px 30px}
.btn-dark{background:var(--ink);color:var(--white)}

/* Hero */
.hero{top:0;height:660px;background:var(--ink)}
.hero .photo{inset:0;background:linear-gradient(180deg,#4b4f4a 0%,#33352f 45%,#2b3a26 85%,#3e5a2f 100%)}
.brand{position:absolute;left:80px;top:56px;color:var(--white);font-weight:600;letter-spacing:6px;text-transform:uppercase}
.brand .big{font-size:44px;display:block;line-height:1}
.brand .small{font-size:16px;letter-spacing:8px;display:block;margin-top:4px}
.nav{position:absolute;right:150px;top:34px;color:var(--white);font-size:12px;font-weight:600;letter-spacing:2px}
.burger{position:absolute;right:80px;top:30px}
.welcome{position:absolute;left:540px;top:240px;width:548px;height:260px;border:3px solid var(--white)}
.welcome .tag{position:absolute;left:30px;top:130px;transform:translate(-50%,-50%) rotate(-90deg);color:var(--white);font-size:12px;font-weight:600;letter-spacing:5px;white-space:nowrap}
.welcome .divider{position:absolute;left:64px;top:28px;bottom:28px;border-left:2px solid var(--white)}
.welcome h1{position:absolute;left:100px;top:70px;color:var(--white);font-size:30px;font-weight:600}
.welcome p{position:absolute;left:100px;top:120px;width:420px;color:var(--white);font-size:14px;line-height:22px}
.welcome .btn{position:absolute;left:100px;top:176px;padding:10px 22px;font-size:11px}
.scroll-tag{position:absolute;right:36px;top:370px;transform:rotate(90deg);transform-origin:right top;color:var(--white);font-size:11px;letter-spacing:4px}
.scroll-dot{position:absolute;left:586px;top:592px;width:28px;height:28px;border-radius:50%;background:var(--ink)}

/* Overview */
.overview{top:660px;height:532px;background:var(--grey-light)}
.overview .copy{position:absolute;left:192px;top:96px;width:360px}
.overview .photo{left:600px;top:0;width:600px;height:532px;background:linear-gradient(160deg,#d9d2c4 0%,#cfc3a8 40%,#b59c7e 100%)}

/* Featured */
.featured{top:1192px;height:528px;background:var(--ink)}
.featured .photo{left:0;top:0;width:600px;height:528px;background:linear-gradient(180deg,#eef0f0 0%,#d5d9da 45%,#7b7e79 70%,#3f4a3a 100%)}
.featured .copy{position:absolute;left:672px;top:84px;width:440px}
.featured .label{color:var(--gold);font-size:14px;font-weight:600;letter-spacing:3px}
.featured h2{color:var(--white);font-size:30px;font-weight:500;line-height:40px;margin-top:20px}
.featured h2 .price{color:var(--gold)}
.featured p{color:#bdbdbd;font-size:14px;line-height:24px;margin-top:26px}
.specs{display:flex;gap:28px;margin-top:28px;color:var(--white);font-size:11px;letter-spacing:1px}
.specs span{display:flex;align-items:center;gap:8px}
.featured .btn{margin-top:34px;padding:12px 24px;font-size:11px}

/* Reviews */
.reviews{top:1720px;height:600px;background:var(--white);text-align:center}
.section-head{position:absolute;left:0;width:1200px;top:70px;text-align:center}
.section-head .kicker{margin-top:8px}
.review{position:absolute;top:200px;width:320px;text-align:left}
.review .avatar{width:100px;height:100px;border-radius:50%;margin-left:6px}
.review .who{font-size:15px;color:var(--ink);font-weight:600;margin-top:20px}
.review .who small{font-weight:400;color:var(--grey)}
.review p{font-size:14px;line-height:24px;margin-top:10px}
.stars{display:flex;gap:4px;margin-top:14px}
.arrow{position:absolute}

/* Rescue */
.rescue{top:2320px;height:528px;background:var(--grey-light)}
.rescue .copy{position:absolute;left:192px;top:92px;width:360px}
.rescue .photo{left:600px;top:0;width:600px;height:528px;background:linear-gradient(150deg,#c9c4bb 0%,#e2d3b4 50%,#b99a6a 100%)}

/* Blog */
.blog{top:2848px;height:600px;background:var(--white)}
.post{position:absolute;top:214px;width:368px;background:var(--white);box-shadow:0 2px 10px rgba(0,0,0,.08)}
.post .photo{position:relative;height:180px}
.post .date{display:inline-block;background:var(--ink);color:var(--white);font-size:10px;letter-spacing:1px;padding:5px 12px;margin:14px 0 0 20px}
.post h3{font-size:16px;font-weight:600;color:var(--ink);margin:14px 20px 0;line-height:22px}
.post p{font-size:13px;line-height:21px;margin:10px 20px 22px}

/* Contact */
.contact{top:3448px;height:576px;background:var(--ink)}
.contact .photo{inset:0;background:linear-gradient(180deg,#2c2926 0%,#1d1b1a 100%)}
.contact .copy{position:absolute;left:192px;top:96px;width:380px;color:var(--white)}
.contact .script{color:var(--white)}
.contact .kicker{color:var(--white)}
.contact .info{font-size:13px;line-height:20px;margin-top:22px;color:#cfcfcf}
.contact .info b{display:block;color:var(--white);font-size:20px;font-weight:500}
.socials{display:flex;gap:10px;margin-top:26px}
.socials span{width:26px;height:26px;border-radius:50%}
.copyright{font-size:12px;color:#bdbdbd;margin-top:26px;line-height:20px}
.copyright a{color:var(--gold);text-decoration:none}
.form{position:absolute;left:680px;top:96px;width:420px}
.field{border-bottom:1px solid #5b5753;color:#cfcfcf;font-size:14px;padding:10px 0;margin-bottom:34px}
.field.tall{height:90px}
.form .btn{padding:10px 24px;font-size:11px}
.to-top{position:absolute;right:36px;bottom:36px}
</style>
</head>
<body>

<section class="hero">
  <div class="photo" role="img" aria-label="Mid-century home at dusk with glass walls and a garden"></div>
  <div class="brand"><span class="big">Halvor</span><span class="small">Real Estate</span></div>
  <div class="nav">PROPERTY</div>
  <svg class="burger" width="30" height="22" viewBox="0 0 30 22"><g stroke="#fff" stroke-width="3"><line x1="0" y1="3" x2="30" y2="3"/><line x1="0" y1="11" x2="30" y2="11"/><line x1="0" y1="19" x2="30" y2="19"/></g></svg>
  <div class="welcome">
    <span class="tag">WELCOME TO</span>
    <span class="divider"></span>
    <h1>Halvor Real Estate</h1>
    <p>Delia Halvor, Realtor, Mid-Century Specialist<br>Homes San Diego, Ca</p>
    <span class="btn">View Collection</span>
  </div>
  <div class="scroll-tag">SCROLL</div>
  <div class="scroll-dot"></div>
</section>

<section class="overview">
  <div class="copy">
    <div class="script">Overview</div>
    <div class="kicker">Meet Delia</div>
    <p class="body-copy" style="margin-top:20px">For as long as I can remember, I have always had a deep love and admiration for our Armed Forces. The fact that these brave men and women volunteer to put their lives on the line to protect our freedom is astounding to me. I knew that when I became a Realtor...</p>
    <span class="btn" style="margin-top:30px">Discover More</span>
  </div>
  <div class="photo" role="img" aria-label="Portrait photo of the realtor"></div>
</section>

<section class="featured">
  <div class="photo" role="img" aria-label="Modern timber and white house with a car in the driveway"></div>
  <div class="copy">
    <div class="label">FEATURED PROPERTIES</div>
    <h2>14 Coralwood Lane, Ridgeview Point, 2031 - <span class="price">$590,000</span></h2>
    <p>Displaying the sense of size, privacy and exclusivity of a house, this stylishly appointed courtyard residence offers a generously...</p>
    <div class="specs">
      <span><svg width="20" height="14" viewBox="0 0 20 14"><rect x="1" y="5" width="18" height="6" fill="none" stroke="#fff" stroke-width="1.5"/><line x1="1" y1="13" x2="1" y2="2" stroke="#fff" stroke-width="1.5"/></svg>3 BED</span>
      <span><svg width="18" height="14" viewBox="0 0 18 14"><path d="M1 7h16v3a3 3 0 0 1-3 3H4a3 3 0 0 1-3-3z" fill="none" stroke="#fff" stroke-width="1.5"/></svg>2 BATH</span>
      <span><svg width="20" height="14" viewBox="0 0 20 14"><path d="M2 10l2-6h12l2 6v3H2z" fill="none" stroke="#fff" stroke-width="1.5"/></svg>2 GARAGE</span>
    </div>
    <span class="btn">Explore More</span>
  </div>
</section>

<section class="reviews">
  <div class="section-head">
    <div class="script">Reviews</div>
    <div class="kicker">What our customer say</div>
  </div>
  <svg class="arrow" style="left:136px;top:310px" width="20" height="32" viewBox="0 0 20 32"><polyline points="16,2 4,16 16,30" fill="none" stroke="#999" stroke-width="3"/></svg>
  <div class="review" style="left:210px">
    <div class="avatar" role="img" aria-label="Client photo" style="background:linear-gradient(160deg,#9aa7b3,#4c5968)"></div>
    <div class="who">Marla P. <small>/ Last Week</small></div>
    <p>My husband and I are so very thankful and blessed to have had Delia as our realtor when we sold our home in Santee. Delia is easy to work with, efficient and above everything else...</p>
    <div class="stars"><svg width="90" height="14" viewBox="0 0 90 14"><g fill="#e8b931"><polygon points="7,0 9,5 14,5 10,8 11,13 7,10 3,13 4,8 0,5 5,5"/><polygon transform="translate(18 0)" points="7,0 9,5 14,5 10,8 11,13 7,10 3,13 4,8 0,5 5,5"/><polygon transform="translate(36 0)" points="7,0 9,5 14,5 10,8 11,13 7,10 3,13 4,8 0,5 5,5"/><polygon transform="translate(54 0)" points="7,0 9,5 14,5 10,8 11,13 7,10 3,13 4,8 0,5 5,5"/></g><polygon transform="translate(72 0)" fill="#ccc" points="7,0 9,5 14,5 10,8 11,13 7,10 3,13 4,8 0,5 5,5"/></svg></div>
  </div>
  <div class="review" style="left:680px">
    <div class="avatar" role="img" aria-label="Client photo" style="background:linear-gradient(160deg,#e6d2bd,#8b6a52)"></div>
    <div class="who">Renata G. <small>/ Year Ago</small></div>
    <p>When my partner and I began our house hunt we originally used a different agent. We quickly dropped them after they ignored our calls, and didn't seem to care about us...</p>
    <div class="stars"><svg width="90" height="14" viewBox="0 0 90 14"><g fill="#e8b931"><polygon points="7,0 9,5 14,5 10,8 11,13 7,10 3,13 4,8 0,5 5,5"/><polygon transform="translate(18 0)" points="7,0 9,5 14,5 10,8 11,13 7,10 3,13 4,8 0,5 5,5"/><polygon transform="translate(36 0)" points="7,0 9,5 14,5 10,8 11,13 7,10 3,13 4,8 0,5 5,5"/><polygon transform="translate(54 0)" points="7,0 9,5 14,5 10,8 11,13 7,10 3,13 4,8 0,5 5,5"/></g><polygon transform="translate(72 0)" fill="#ccc" points="7,0 9,5 14,5 10,8 11,13 7,10 3,13 4,8 0,5 5,5"/></svg></div>
  </div>
  <svg class="arrow" style="left:1062px;top:310px" width="20" height="32" viewBox="0 0 20 32"><polyline points="4,2 16,16 4,30" fill="none" stroke="#333" stroke-width="3"/></svg>
</section>

<section class="rescue">
  <div class="copy">
    <div class="script">Rescue</div>
    <div class="kicker" style="line-height:26px">Co-founder of the<br>Paw Haven</div>
    <p class="body-copy" style="margin-top:20px">Since childhood, my number one passion has been animal advocacy. In case you were wondering, yes, I was the girl who made all the frog dissection in Biology class. When I co-founded The Paw Haven in 2012 my dream of saving dogs in need was finally realized.</p>
    <span class="btn btn-dark" style="margin-top:30px">Discover More</span>
  </div>
  <div class="photo" role="img" aria-label="Realtor holding a golden puppy"></div>
</section>

<section class="blog">
  <div class="section-head">
    <div class="script">Blog</div>
    <div class="kicker">Read our latest update</div>
  </div>
  <svg class="arrow" style="left:104px;top:360px" width="20" height="32" viewBox="0 0 20 32"><polyline points="16,2 4,16 16,30" fill="none" stroke="#999" stroke-width="3"/></svg>
  <article class="post" style="left:192px">
    <div class="photo" role="img" aria-label="Tall residential building against a blue sky" style="background:linear-gradient(180deg,#6d8fb3,#384a5f)"></div>
    <span class="date">24 APR, 2016</span>
    <h3>Cedar Hill: SD's New Real Estate Hot Spot</h3>
    <p>Cedar Hill: What is there to love? Our latest in central San Diego, near famous Balboa Park and...</p>
  </article>
  <article class="post" style="left:640px">
    <div class="photo" role="img" aria-label="Party table with blue napkins and treats" style="background:linear-gradient(160deg,#4aa0c2,#e0cfa0)"></div>
    <span class="date">25 APR, 2016</span>
    <h3>How To Be The Hostess With The Mostess</h3>
    <p>We all need to pop those corks at some point, so here's a few tips on how to pull off a great dinner party!</p>
  </article>
  <svg class="arrow" style="left:1072px;top:360px" width="20" height="32" viewBox="0 0 20 32"><polyline points="4,2 16,16 4,30" fill="none" stroke="#999" stroke-width="3"/></svg>
</section>

<section class="contact">
  <div class="photo" role="img" aria-label="Dark interior background"></div>
  <div class="copy">
    <div class="script">Contact</div>
    <div class="kicker">Get in touch</div>
    <div class="info">Call Us<b>858-555-0147</b></div>
    <div class="info">Email<br>hello@halvorhomes.com</div>
    <div class="info">Location<br>1742 Harbor St, San Diego<br>Ca 92101</div>
    <div class="socials"><span style="background:#3b5998"></span><span style="background:#1da1f2"></span><span style="background:#e1306c"></span><span style="background:#d34836"></span></div>
    <div class="copyright">© Copyright 2017 Halvor Real Estate<br><a>TERMS OF USE</a> | PRIVACY POLICY</div>
  </div>
  <div class="form">
    <div class="field">Your Name</div>
    <div class="field">Your Email</div>
    <div class="field">Subject</div>
    <div class="field tall">Your Message</div>
    <span class="btn">&#9992; Send</span>
  </div>
  <svg class="to-top" width="36" height="26" viewBox="0 0 36 26"><polygon points="18,0 36,26 0,26" fill="#e8b931"/></svg>
</section>

</body>
</html>
```